Sale of South Sea and Tahitian Pearl Jewellery, online business

I need a business card designed for my website business. We sell South Sea and Tahitian Pearl Jewellery. The colour theme for the website is black and white and would like to carry this through to business cards. Our brand is very elegant and stylish, would like sketch picture of women or fashion involving pearls if not the sketched picture then have the card very plan. below are pictures of the ideas I like and also the logo and writing that is used on my jewellery boxes.
Font is English Hand DB

Target Market(s)

30 and over women in the high end of the market

Industry/Entity Type

Business

Contact Information for Business Card

Business name - Varno Gems( front of card)
Back of card -Details
Rosalind Thackery
Gemmologist MDRS
email: rosalind@varnogems.com.au
website: varnogems.com.au
mob: +61 427 508 193
Perth Australia

Varno Stelle PTY T/AS Varno Gems
ABN 47 283 915 604

Colors
1b1b1b
ffffff
85cae6

Requirements
Must have
• Black and white colour preferably black card with white writing and picture.
• The Same writing as logo and writing on box packaging, attached a file with writing.
• Business name on one side of the card and all other details on the other side.
• Can have tiny hints of the harbour blue colour.
• Font: English Hand DB
Nice to have
• I really like the idea of having a sketch of a stylish or elegent lady wearing pearls or a sketch of a pearl, if not the sketch a really plain and simple card.
Should not have
• busy patterns.

```html
<!DOCTYPE html>
<html lang="en">
<head>
<meta charset="utf-8">
<title>Varno Gems – Business Card</title>
<link href="https://fonts.googleapis.com/css2?family=Pinyon+Script&family=Bodoni+Moda:wght@400&family=Josefin+Sans:wght@300;600&display=swap" rel="stylesheet">
<style>
  :root {
    --ink: #1b1b1b;
    --card-dark: #231f20;
    --paper: #ffffff;
    --sketch-tone-a: #ffffff;
    --sketch-tone-b: #ededed;
  }
  html, body {
    margin: 0;
    padding: 0;
    overflow: hidden;
    background: var(--paper);
  }
  .sheet {
    position: relative;
    width: 1043px;
    height: 1200px;
    background: var(--paper);
    overflow: hidden;
  }
  .panel { position: absolute; }
  .panel--front-sketch { left: 0; top: 0; width: 518px; height: 598px; background: var(--paper); }
  .panel--front-dark { left: 523px; top: 0; width: 520px; height: 598px; background: var(--card-dark); color: var(--paper); }
  .panel--logo-light { left: 0; top: 607px; width: 518px; height: 593px; background: var(--paper); color: var(--ink); }
  .panel--details { left: 523px; top: 607px; width: 520px; height: 593px; background: var(--card-dark); color: var(--paper); }

  .sketch-area {
    position: absolute;
    left: 58px;
    top: 112px;
    width: 400px;
    height: 396px;
    background: radial-gradient(ellipse at 50% 45%, var(--sketch-tone-b) 0%, var(--sketch-tone-a) 72%);
  }

  .brand-ring {
    position: absolute;
    box-sizing: border-box;
    border-radius: 50%;
    border: 4px solid currentColor;
    display: flex;
    align-items: center;
    justify-content: center;
  }
  .panel--front-dark .brand-ring { left: 112px; top: 85px; width: 316px; height: 316px; }
  .panel--logo-light .brand-ring { left: 107px; top: 94px; width: 320px; height: 320px; }

  .brand-ring__name {
    margin: 0;
    font-family: "Pinyon Script", cursive;
    font-weight: 400;
    font-size: 50px;
    line-height: 1;
  }

  .brand-name {
    position: absolute;
    left: 0;
    width: 100%;
    text-align: center;
    font-family: "Pinyon Script", cursive;
    font-weight: 400;
    font-size: 66px;
    margin: 0;
    line-height: 1;
  }
  .panel--front-dark .brand-name { top: 470px; left: 12px; }
  .panel--logo-light .brand-name { top: 476px; left: 8px; }

  .holder {
    position: absolute;
    right: 60px;
    top: 98px;
    text-align: right;
  }
  .holder__name {
    margin: 0;
    font-family: "Bodoni Moda", serif;
    font-weight: 400;
    font-size: 47px;
    line-height: 1;
  }
  .holder__title {
    margin: 16px 0 0;
    font-family: "Josefin Sans", sans-serif;
    font-weight: 300;
    font-size: 28px;
    line-height: 1;
  }

  .contact {
    position: absolute;
    right: 60px;
    top: 404px;
    margin: 0;
    padding: 0;
    list-style: none;
    text-align: right;
    font-family: "Josefin Sans", sans-serif;
    font-weight: 300;
    font-size: 23px;
    line-height: 33px;
  }
  .contact__label { font-weight: 600; }
</style>
</head>
<body>
  <main class="sheet">
    <section class="panel panel--front-sketch">
      <div class="sketch-area" role="img" aria-label="Line sketch of an elegant lady in a wide-brimmed hat wearing a pearl necklace"></div>
    </section>

    <section class="panel panel--front-dark">
      <div class="brand-ring"><p class="brand-ring__name">Varno Gems</p></div>
      <p class="brand-name">Varno Gems</p>
    </section>

    <section class="panel panel--logo-light">
      <div class="brand-ring"><p class="brand-ring__name">Varno Gems</p></div>
      <p class="brand-name">Varno Gems</p>
    </section>

    <section class="panel panel--details">
      <div class="holder">
        <h1 class="holder__name">Rosalind Thackery</h1>
        <p class="holder__title">Gemmologist MDRS</p>
      </div>
      <ul class="contact">
        <li>Perth Australia</li>
        <li><span class="contact__label">mob:</span> +61 427 508 193</li>
        <li><span class="contact__label">email:</span> rosalind@varnogems.com.au</li>
        <li><span class="contact__label">web:</span> varnogems.com.au</li>
      </ul>
    </section>
  </main>
</body>
</html>
```